truck and trailer business Wrap Design

needing a redisgn of our truck and trailer wraps, i have attached the current trailer wrap design and pictures of the new trailer needing a wrap design. trailer is 26ft v nose. 8.5 wide and 7.5ft tall need the trucks that pull the trailers to match. 2018 q-380 long bed. i have attached pictures of the truck. 2009 ZEMO 26 FT BOX

Industry/Entity Type

Insulation

Colors

Designer to choose colors to be used in the design.

Requirements
Must have
• wrap needs to be unique and stand out like our current wrap

```html
<!DOCTYPE html>
<html lang="en">
<head>
<meta charset="utf-8">
<title>Summit Spray Foam – Trailer Wrap</title>
<link rel="stylesheet" href="https://fonts.googleapis.com/css2?family=Michroma&display=swap">
<style>
  :root {
    --page: #ffffff;
    --white: #ffffff;
    --ink: #111111;
    --brand-blue: #1f5cc4;
    --sky-blue: #3b9be0;
    --deep-blue: #17418f;
    --navy: #0e1c28;
    --charcoal: #2b2b2b;
    --charcoal-dark: #1c1c1c;
    --attic-warm: #8a5a34;
    --attic-dark: #4a2e1a;
    --foam-light: #d9d2c4;
    --foam-tan: #b89a70;
  }
  html, body {
    margin: 0;
    width: 1200px;
    height: 1200px;
    overflow: hidden;
    background: var(--page);
  }
  .canvas {
    position: relative;
    width: 1200px;
    height: 1200px;
    display: flex;
    align-items: center;
    justify-content: center;
  }
  .wrap-panel {
    width: 1130px;
    height: auto;
    display: block;
  }
  .service-line {
    font-family: "Michroma", sans-serif;
    font-size: 15px;
    letter-spacing: 1px;
    fill: var(--ink);
  }
  .brand-name {
    font-family: "Michroma", sans-serif;
    font-size: 30px;
    letter-spacing: 1px;
    fill: var(--brand-blue);
  }
  .web-address {
    font-family: "Michroma", sans-serif;
    font-size: 18px;
    letter-spacing: 1px;
    fill: var(--white);
  }
  .phone-number {
    font-family: "Michroma", sans-serif;
    font-size: 31px;
    letter-spacing: 5px;
    fill: var(--white);
  }
</style>
</head>
<body>
<main class="canvas">
  <svg class="wrap-panel" viewBox="0 0 1278 432" xmlns="http://www.w3.org/2000/svg">
    <defs>
      <linearGradient id="band-dark" x1="0" y1="0" x2="1" y2="1">
        <stop offset="0" stop-color="var(--charcoal)"/>
        <stop offset="1" stop-color="var(--charcoal-dark)"/>
      </linearGradient>
      <linearGradient id="attic-tones" x1="0" y1="0" x2="1" y2="1">
        <stop offset="0" stop-color="var(--attic-dark)"/>
        <stop offset="0.5" stop-color="var(--attic-warm)"/>
        <stop offset="1" stop-color="var(--foam-tan)"/>
      </linearGradient>
      <linearGradient id="ceiling-tones" x1="0" y1="0" x2="0" y2="1">
        <stop offset="0" stop-color="var(--foam-light)"/>
        <stop offset="1" stop-color="var(--foam-tan)"/>
      </linearGradient>
      <linearGradient id="wall-tones" x1="0" y1="0" x2="1" y2="1">
        <stop offset="0" stop-color="var(--foam-light)"/>
        <stop offset="1" stop-color="#c9a57a"/>
      </linearGradient>
    </defs>

    <!-- base -->
    <rect class="panel-base" width="1278" height="432" fill="var(--navy)"/>

    <!-- white header area with blue edge -->
    <polygon class="header-edge" points="0,0 735,0 590,150 0,150" fill="var(--brand-blue)"/>
    <polygon class="header-area" points="0,0 708,0 570,143 0,143" fill="var(--white)"/>

    <!-- dark contact band -->
    <path class="contact-band" d="M0,143 L572,143 L490,240 Q455,285 500,330 L520,350 L0,350 Z" fill="url(#band-dark)"/>
    <path class="white-swoosh" d="M572,143 L585,143 L500,245 Q470,290 515,335 L660,432 L630,432 L505,345 Q448,290 488,238 Z" fill="var(--white)"/>
    <rect class="divider-line" x="135" y="343" width="390" height="4" fill="var(--white)"/>
    <path class="bottom-band" d="M0,350 L520,350 L640,432 L0,432 Z" fill="var(--charcoal-dark)"/>

    <!-- blue sweeps lower left -->
    <path class="sweep-deep" d="M0,245 Q60,360 300,432 L420,432 Q120,380 0,220 Z" fill="var(--deep-blue)"/>
    <path class="sweep-sky" d="M0,280 Q50,390 200,432 L330,432 Q90,390 0,270 Z" fill="var(--sky-blue)"/>
    <path class="sweep-brand" d="M0,330 Q30,410 110,432 L190,432 Q50,400 0,310 Z" fill="var(--brand-blue)"/>

    <!-- photo areas -->
    <g role="img" aria-label="Photo of an installer in protective suit blowing loose-fill insulation between attic joists">
      <path d="M560,200 L765,8 Q782,-4 800,6 L1015,140 Q1035,156 1024,182 L905,432 L640,432 L545,300 Q528,255 560,200 Z"
            fill="url(#attic-tones)" stroke="var(--brand-blue)" stroke-width="9"/>
    </g>
    <g role="img" aria-label="Photo of spray foam applied to a ceiling between wooden rafters">
      <path d="M1012,25 Q1018,12 1040,14 L1278,14 L1278,205 L1200,236 Q1180,246 1160,230 L1018,104 Q1002,84 1012,25 Z"
            fill="url(#ceiling-tones)" stroke="var(--brand-blue)" stroke-width="9"/>
    </g>
    <g role="img" aria-label="Photo of a wall cavity filled with spray foam insulation">
      <path d="M982,300 L1130,202 Q1150,190 1170,200 L1278,262 L1278,432 L1002,432 Q968,398 982,300 Z"
            fill="url(#wall-tones)" stroke="var(--brand-blue)" stroke-width="9"/>
    </g>

    <!-- text -->
    <text class="service-line" x="13" y="25">SPRAY FOAM . FIBERGLASS . INSULATION . ROOFING</text>

    <rect class="brand-rule" x="95" y="52" width="420" height="2" fill="var(--ink)"/>
    <text class="brand-name" x="305" y="100" text-anchor="middle">SUMMIT SPRAY FOAM</text>
    <rect class="brand-rule" x="95" y="121" width="420" height="2" fill="var(--ink)"/>

    <text class="web-address" x="285" y="214" text-anchor="middle">SUMMITSPRAYFOAM.NET</text>
    <text class="phone-number" x="280" y="262" text-anchor="middle">555-010-4827</text>
  </svg>
</main>
</body>
</html>
```